Medical Practice Business Card

we need a business card for our new medical ophthalmology practice based in Needham Massachusetts. we are looking for a simple , modern and elegant design.
the card needs to contain the following
1- the logo of our practice (please see attached file)
2- the name of the practice : "Silver Birch Retina Care"
3- Doctor's Name: Tobias Rendell MD PhD
4- Specialty: Board-Certified Vitreoretinal Surgeon
5- practice address: 87 Larkspur Ave, Suite 210, Alder Falls VT 05609
7- Office number: 617- 482 - 7730
8- fax number: 617- 391 - 2268
9- email: info@sbretinahub.example
10- website: www.sbretinahub.example

```html
<!DOCTYPE html>
<html lang="en">
<head>
<meta charset="utf-8">
<title>Silver Birch Retina Care – Business Card</title>
<link href="https://fonts.googleapis.com/css2?family=Nunito:wght@400;600;800&display=swap" rel="stylesheet">
<style>
  :root {
    --backdrop: #7f95b8;
    --paper: #ffffff;
    --navy: #24456e;
    --ink: #2f4a6d;
    --accent: #6cc4dc;
    --teal-deep: #2f5577;
    --teal-mid: #5f9fb3;
    --teal-light: #86d3e2;
    --logo-ring: #4a86c6;
  }
  * { box-sizing: border-box; margin: 0; padding: 0; }
  html, body {
    width: 1200px; height: 876px; overflow: hidden;
    background: var(--backdrop);
    font-family: "Nunito", sans-serif;
  }
  .stage {
    width: 1200px; height: 876px;
    display: flex; align-items: center; justify-content: center; gap: 60px;
  }
  .card {
    position: relative;
    width: 525px; height: 300px;
    border-radius: 4px;
    box-shadow: 0 14px 30px rgba(30, 45, 80, .28);
    overflow: hidden;
  }
  .card--front { background: var(--paper); color: var(--ink); }
  .card--back {
    background: linear-gradient(110deg, var(--teal-deep) 0%, var(--teal-mid) 48%, var(--teal-light) 100%);
  }

  .practice-mark {
    display: flex; align-items: center; gap: 10px;
    color: var(--navy); font-weight: 600; letter-spacing: .5px;
    white-space: nowrap;
  }
  .practice-mark__dot {
    width: 14px; height: 14px; border-radius: 50%;
    background: var(--logo-ring); flex: none;
  }

  .doctor {
    position: absolute; top: 36px; right: 46px; width: 300px;
  }
  .doctor__name { font-weight: 800; font-size: 21px; color: var(--navy); line-height: 1.15; }
  .doctor__title { font-size: 13px; color: var(--ink); margin-top: 2px; }

  .card--front .practice-mark {
    position: absolute; top: 122px; left: 150px; font-size: 23px;
  }

  .contacts {
    position: absolute; left: 30px; bottom: 34px;
    font-size: 14px; color: var(--ink);
  }
  .contacts__row { display: flex; align-items: center; gap: 6px; margin-top: 6px; white-space: nowrap; }
  .contacts__item { display: inline-flex; align-items: center; gap: 4px; }
  .icon { width: 14px; height: 14px; flex: none; }

  .card--back .practice-mark {
    position: absolute; top: 112px; left: 150px; font-size: 27px;
  }
  .website {
    position: absolute; left: 40px; bottom: 44px;
    color: #ffffff; font-size: 15px; letter-spacing: 6px; white-space: nowrap;
  }
</style>
</head>
<body>
<main class="stage">
  <section class="card card--front" aria-label="Business card front">
    <div class="doctor">
      <p class="doctor__name">Tobias Rendell MD PhD</p>
      <p class="doctor__title">Board-Certified Vitreoretinal Surgeon</p>
    </div>

    <div class="practice-mark">
      <span class="practice-mark__dot"></span>
      <span>Silver Birch Retina Care</span>
    </div>

    <div class="contacts">
      <div class="contacts__row">
        <span class="contacts__item">
          <svg class="icon" viewBox="0 0 14 14" aria-hidden="true"><circle cx="7" cy="7" r="7" fill="var(--accent)"/><path d="M4.5 3.8h1.4l.6 1.6-.8.6a4 4 0 0 0 2.3 2.3l.6-.8 1.6.6v1.4a.6.6 0 0 1-.6.6A5.7 5.7 0 0 1 3.9 4.4a.6.6 0 0 1 .6-.6z" fill="#fff"/></svg>
          617- 482 - 7730
        </span>
        <span class="contacts__item">
          <svg class="icon" viewBox="0 0 14 14" aria-hidden="true"><circle cx="7" cy="7" r="7" fill="var(--accent)"/><rect x="4" y="5.5" width="6" height="4" rx=".6" fill="#fff"/><rect x="5" y="3.5" width="4" height="2" fill="#fff"/></svg>
          617- 391 - 2268
        </span>
        <span class="contacts__item">
          <svg class="icon" viewBox="0 0 14 14" aria-hidden="true"><circle cx="7" cy="7" r="7" fill="var(--accent)"/><rect x="3.8" y="4.6" width="6.4" height="4.8" rx=".6" fill="#fff"/><path d="M3.9 4.8 7 7.3l3.1-2.5" stroke="var(--accent)" stroke-width=".8" fill="none"/></svg>
          info@sbretinahub.example
        </span>
      </div>
      <div class="contacts__row">
        <span class="contacts__item">
          <svg class="icon" viewBox="0 0 14 14" aria-hidden="true"><circle cx="7" cy="7" r="7" fill="var(--accent)"/><path d="M7 3a2.4 2.4 0 0 1 2.4 2.4C9.4 7.2 7 10.6 7 10.6S4.6 7.2 4.6 5.4A2.4 2.4 0 0 1 7 3z" fill="#fff"/><circle cx="7" cy="5.4" r=".9" fill="var(--accent)"/></svg>
          87 Larkspur Ave, Suite 210, Alder Falls VT 05609
        </span>
      </div>
    </div>
  </section>

  <section class="card card--back" aria-label="Business card back">
    <div class="practice-mark">
      <span class="practice-mark__dot"></span>
      <span>Silver Birch Retina Care</span>
    </div>
    <p class="website">www.sbretinahub.example</p>
  </section>
</main>
</body>
</html>
```